New Signage Design Project for Qb Dale Outworks *

Im Looking for yard design with our logo, number, website, services & credentials. Each Yard sign will be for 3 different titles...

Example 1: New Roof Coming Soon (Title) This Yardsign is for projects before we start them... Letting neighbors know why we are going to be there.
Example 2: New Roof In progress (Title) This Yardsign is for during the process of the work.. letting neighbors know what we working on!!
Example 3: This Design is only for the customer that says a title NEW ROOF INSTALL SATISFIED CUSTOMER ON THIS DESIGN I DONT NEED SERVICES JSUT LOGO AND THE TITLE

Target Market(s)

Customers

Industry/Entity Type

Roofing

Font styles to use
Serif
Sans Serif

Colors
33b8a4
5c5c5c

Requirements
Must have
• -LOGO
• -WEBSITE
• -NUMBER
• -TITLES
• -SERVICES (ROOFING, GUTTERS, PAINTING, PRESSURE WASHING, EXTERIOR DESIGN.)
• -CREDENTIALS
• -HOUSE SHAPE DESIGN
• -LOGO COLORS
• -NOT BUSY BUT CLEAN AND SHARP
• -MATTE COLORS
Nice to have
• Easy To read, Eye Catchy, Clean Design, logo colors, titles
Should not have
• not Busy,

```html
<!DOCTYPE html>
<html lang="en">
<head>
<meta charset="utf-8">
<title>Qb Dale Outworks – Yard Signs</title>
<link rel="stylesheet" href="https://fonts.googleapis.com/css2?family=Barlow+Semi+Condensed:wght@600;700;800&display=swap">
<style>
  :root {
    --teal: #1a9384;
    --charcoal: #323133;
    --white: #ffffff;
    --ink: #2c2c2e;
    --page: #ffffff;
    --badge: #f2f2f2;
  }
  * { margin: 0; padding: 0; box-sizing: border-box; }
  html, body { width: 1200px; height: 1200px; overflow: hidden; background: var(--page); }
  body { position: relative; font-family: "Barlow Semi Condensed", "Arial Narrow", sans-serif; }

  .yard-sign {
    position: absolute;
    background: var(--charcoal);
    container-type: size;
    overflow: hidden;
  }
  .yard-sign--hero { left: 230px; top: 102px; width: 748px; height: 490px; }
  .yard-sign--small { top: 922px; width: 369px; height: 216px; }
  .yard-sign--one { left: 41px; }
  .yard-sign--two { left: 423px; }
  .yard-sign--three { left: 805px; }

  .brand {
    position: absolute; left: 4%; top: 8%; width: 18%; height: 26%;
    display: flex; flex-direction: column; align-items: center; justify-content: center; gap: 3cqh;
  }
  .brand__mark { width: 9cqh; height: 9cqh; background: var(--teal); }
  .brand__name {
    color: var(--teal); font-weight: 700; font-size: 4.8cqh; line-height: 1.05; text-align: center; white-space: nowrap;
  }

  .services {
    position: absolute; left: 24.5%; right: 0; top: 6.2%; height: 27%;
    background: var(--white);
    padding-left: 2.7%;
    display: flex; flex-direction: column; justify-content: center;
    font-weight: 800; font-size: 6cqh; line-height: 1.28; color: var(--ink);
    letter-spacing: 0.02em; white-space: nowrap;
  }
  .services__label { color: var(--teal); }

  .headline {
    position: absolute; left: 24.5%; top: 36%; width: 58%;
    text-align: center; font-weight: 800; line-height: 1; white-space: nowrap;
  }
  .headline__lead { display: block; color: var(--teal); font-size: 18cqh; }
  .headline__status { display: block; color: var(--white); font-size: 15.5cqh; margin-top: 1.5cqh; }

  .phone {
    position: absolute; left: 0; top: 72.3%; width: 61%; height: 18.5%;
    background: var(--teal); color: var(--white);
    display: flex; align-items: center; justify-content: center;
    font-weight: 800; font-size: 15.5cqh; letter-spacing: 0.01em; white-space: nowrap;
  }
  .website {
    position: absolute; left: 3.2%; top: 92.2%;
    color: var(--white); font-weight: 700; font-size: 5cqh; letter-spacing: 0.02em; white-space: nowrap;
  }
  .credential { position: absolute; background: var(--badge); }
  .credential--bureau { left: 70.3%; top: 75.7%; width: 4.5%; height: 12%; }
  .credential--maker { left: 77.6%; top: 76.7%; width: 15.6%; height: 10.2%; }

  /* Satisfied customer variant */
  .install-title {
    position: absolute; left: 24.5%; right: 0; top: 7.4%; height: 26.6%;
    background: var(--white);
    display: flex; align-items: center; justify-content: center;
    color: var(--teal); font-weight: 800; font-size: 21cqh; line-height: 1; white-space: nowrap;
  }
  .install-sub {
    position: absolute; left: 22%; width: 58%; top: 35%;
    text-align: center; font-weight: 800; line-height: 1; white-space: nowrap;
  }
  .install-sub__word { display: block; color: var(--teal); font-size: 21cqh; }
  .install-sub__note { display: block; color: var(--white); font-size: 10cqh; margin-top: 2cqh; letter-spacing: 0.02em; }
</style>
</head>
<body>

  <section class="yard-sign yard-sign--hero" aria-label="New roof coming soon sign">
    <div class="brand"><span class="brand__mark"></span><span class="brand__name">Qb Dale<br>Outworks</span></div>
    <div class="services">
      <span class="services__label">OUR SERVICES</span>
      <span>ROOFING | GUTTERS |PAINTING</span>
      <span>PRESSURE WASHING |EXTERIOR DESIGN</span>
    </div>
    <h1 class="headline"><span class="headline__lead">NEW ROOF</span><span class="headline__status">COMING SOON</span></h1>
    <div class="phone">503-555-0142</div>
    <span class="credential credential--bureau"></span>
    <span class="credential credential--maker"></span>
    <div class="website">www.qbdaleoutworks.com</div>
  </section>

  <section class="yard-sign yard-sign--small yard-sign--one" aria-label="New roof coming soon sign, small">
    <div class="brand"><span class="brand__mark"></span><span class="brand__name">Qb Dale<br>Outworks</span></div>
    <div class="services">
      <span class="services__label">OUR SERVICES</span>
      <span>ROOFING | GUTTERS |PAINTING</span>
      <span>PRESSURE WASHING |EXTERIOR DESIGN</span>
    </div>
    <h2 class="headline"><span class="headline__lead">NEW ROOF</span><span class="headline__status">COMING SOON</span></h2>
    <div class="phone">503-555-0142</div>
    <span class="credential credential--bureau"></span>
    <span class="credential credential--maker"></span>
    <div class="website">www.qbdaleoutworks.com</div>
  </section>

  <section class="yard-sign yard-sign--small yard-sign--two" aria-label="New roof in progress sign">
    <div class="brand"><span class="brand__mark"></span><span class="brand__name">Qb Dale<br>Outworks</span></div>
    <div class="services">
      <span class="services__label">OUR SERVICES</span>
      <span>ROOFING | GUTTERS |PAINTING</span>
      <span>PRESSURE WASHING |EXTERIOR DESIGN</span>
    </div>
    <h2 class="headline"><span class="headline__lead">NEW ROOF</span><span class="headline__status">IN PROGRESS</span></h2>
    <div class="phone">503-555-0142</div>
    <span class="credential credential--bureau"></span>
    <span class="credential credential--maker"></span>
    <div class="website">www.qbdaleoutworks.com</div>
  </section>

  <section class="yard-sign yard-sign--small yard-sign--three" aria-label="New roof install satisfied customer sign">
    <div class="brand"><span class="brand__mark"></span><span class="brand__name">Qb Dale<br>Outworks</span></div>
    <div class="install-title">NEW ROOF</div>
    <h2 class="install-sub"><span class="install-sub__word">INSTALL</span><span class="install-sub__note">SATISFIED CUSTOMER</span></h2>
    <div class="phone">503-555-0142</div>
    <span class="credential credential--bureau"></span>
    <span class="credential credential--maker"></span>
    <div class="website">www.qbdaleoutworks.com</div>
  </section>

</body>
</html>
```